Travel Itinerary Planning Website Redesign

We have built our own website for a travel itinerary planning service using Wix but are not professional designers. We need help getting over the finish line with a redesign of our website. <br/><br/>We like material design elements, icons and styling. The pages need to flow well one to another and evoke a sense of exclusivity, without giving the impression that it's unattainable. The website doesn't need to keep its current "boxy" format but instead should have a better aesthetic and flow. We're also looking for a complete redesign of the "How It Works" section (shown on two different pages of the website) to be more visually pleasing and easy to understand (maybe using icons or infographic style people). <br/><br/>We already have our logo and selected colors. The copy is also available on the live site as well. The redesign will focus on 4 pages: the homepage and the three service pages (one page per service). The website is currently live at www.trelmavista.com. Fonts should be Helvetica Bold, Regular and Light. Preferred color scheme is attached.

Target Market(s)

Ages 28-65, living in the US, mostly large cities with a desire for well planned, non-group travels

Industry/Entity Type

Travel Industry

Font styles to use
Other font styles liked:
• Helvetica

Colors

Designer to choose colors to be used in the design.

Requirements
Must have
• Make sure to use colors we provided in the attachment and what's on the current website
• Redesign "How it Works"
• Include ambassadors area
• Have a second page that showcases how the "Personal Trip Planning" page should look
Should not have
• No header menu needed for this project

```html
<!DOCTYPE html>
<html lang="en">
<head>
<meta charset="utf-8">
<title>Trelmavista — VIP Trip Planning Services</title>
<link href="https://fonts.googleapis.com/css2?family=Arimo:wght@400;700&display=swap" rel="stylesheet">
<style>
:root{
  --cream:#f9f5ee;
  --sand:#ede5da;
  --espresso:#4d3613;
  --cocoa:#5a3d17;
  --bronze:#7d6236;
  --taupe:#b59b74;
  --gold:#cda050;
  --butter:#fdd88a;
  --clay:#a88a63;
  --ink:#4a3414;
  --text:#5b5045;
  --white:#ffffff;
}
*{box-sizing:border-box;margin:0;padding:0}
html,body{width:1200px;height:4819px;overflow:hidden}
body{position:relative;background:var(--cream);font-family:"Arimo",Helvetica,Arial,sans-serif;color:var(--text)}
.abs{position:absolute}
.center{text-align:center}

/* hero */
.hero{left:0;top:0;width:1200px;height:800px;background:linear-gradient(180deg,#8a7c70 0%,#c8a98a 30%,#a88667 55%,#5e4a3c 80%,#3d332e 100%)}
.brand{left:0;top:20px;width:1200px;text-align:center;color:var(--white);font-weight:700;font-size:30px;letter-spacing:1px}
.hero-title{left:120px;top:450px;color:var(--white);font-weight:700;font-size:44px;line-height:54px}
.hero-sub{left:124px;top:566px;color:var(--white);font-size:12px}
.btn{display:block;background:var(--butter);color:var(--ink);font-size:13px;text-align:center;border-radius:22px}
.hero-btn{left:124px;top:605px;width:161px;height:43px;line-height:43px}

.features{left:124px;top:730px;width:954px;height:255px;display:flex}
.feature{flex:1;color:var(--white);text-align:center;padding:30px 26px 0}
.feature svg{width:44px;height:44px;margin-bottom:16px}
.feature h3{font-size:13px;font-weight:700;line-height:17px;height:38px;margin-bottom:14px}
.feature p{font-size:12px;line-height:19px}
.f1{background:var(--cocoa)}.f2{background:var(--bronze)}.f3{background:var(--taupe)}.f4{background:var(--gold)}

.section-title{left:0;width:1200px;text-align:center;color:var(--ink);font-weight:700;font-size:31px;line-height:39px}

/* services */
.service-card{width:308px;top:1189px;height:486px;text-align:center}
.service-card.raised{background:var(--white);border-radius:6px;box-shadow:0 4px 20px rgba(0,0,0,.12)}
.service-photo{width:271px;height:271px;border-radius:50%;margin:15px auto 0}
.service-card h3{font-size:30px;color:var(--ink);font-weight:400;margin-top:30px}
.service-card p{font-size:12px;line-height:16px;margin:22px 40px 0;height:48px}
.more{font-size:11px;color:var(--gold);text-decoration:underline;display:inline-block;margin-top:22px}

/* how it works */
.how{left:0;top:1778px;width:1200px;height:581px;background:var(--sand)}
.step{width:150px;height:150px;border-radius:50%}
.step-inner{position:absolute;left:33px;top:33px;width:84px;height:84px;border-radius:50%;background:var(--white);display:flex;align-items:center;justify-content:center}
.step-label{font-size:13px;font-weight:700;color:var(--ink);width:240px;text-align:center}
.num{width:30px;height:30px;border-radius:50%;border:2px solid currentColor;font-size:11px;font-weight:700;text-align:center;line-height:26px;background:var(--sand)}

.ready{left:0;top:2359px;width:1200px;height:230px;background:var(--gold)}

/* ambassadors */
.amb{width:240px;text-align:center}
.amb-photo{width:219px;height:219px;border-radius:50%;margin:0 auto;border:3px solid var(--espresso)}
.amb h4{font-size:19px;color:var(--ink);margin-top:30px;font-weight:700}
.amb span{font-size:16px;color:var(--gold)}
.arrow{width:40px;height:40px;border-radius:50%;border:2px solid #c9beb1}

/* resources */
.res-bg{left:0;top:3220px;width:1200px;height:768px;background:var(--sand)}
.post{top:3388px;width:308px;height:497px;background:var(--white);border-radius:6px;box-shadow:0 3px 16px rgba(0,0,0,.12);padding:15px}
.post-photo{height:272px;border-radius:4px;position:relative}
.date{position:absolute;left:14px;top:0;width:28px;height:46px;background:var(--butter);color:var(--white);font-size:11px;text-align:center;padding-top:6px;line-height:14px}
.post h4{font-size:13px;color:var(--ink);margin-top:38px;line-height:16px;display:flex;justify-content:space-between}
.post h4 em{font-style:normal;font-weight:400;color:#c9a7a0;font-size:12px}
.post p{font-size:11px;line-height:15px;margin-top:22px;height:64px}
.post .more{margin-top:18px}

/* newsletter */
.news{left:389px;top:4199px;width:422px;height:41px;border:1.5px solid var(--clay);border-radius:21px}
.news span{position:absolute;left:24px;top:13px;font-size:12px;font-style:italic;color:var(--ink)}
.news .btn{position:absolute;right:0;top:-1px;width:142px;height:41px;line-height:41px;font-size:12px}

/* footer */
.footer{left:0;top:4352px;width:1200px;height:467px;background:var(--clay);color:var(--white)}
.foot-col h5{font-size:19px;font-weight:400;margin-bottom:22px}
.foot-col a{display:block;font-size:12px;color:var(--white);text-decoration:none;margin-bottom:15px}
</style>
</head>
<body>

<!-- hero -->
<div class="abs hero" role="img" aria-label="Photo of Venice: domed basilica and gondolas on the Grand Canal at sunset"></div>
<svg class="abs" style="left:0;top:720px" width="1200" height="90" viewBox="0 0 1200 90"><path fill="#f9f5ee" d="M0 90V40l12 6 10-14 14 10 10-8 18 16 10-10 20 18h1076l18-16 10 10 14-14 12 8 12-6 12 12 14-8 8 4V90z"/></svg>
<div class="abs brand">TRELMAVISTA</div>
<h1 class="abs hero-title">VIP Trip Planning Services<br>For Every Budget</h1>
<p class="abs hero-sub">Trelmavista creates template-free, handcrafted travel itineraries just for you.</p>
<a class="abs btn hero-btn">Get Started</a>

<div class="abs features">
  <div class="feature f1">
    <svg viewBox="0 0 44 44" fill="#fff"><polygon points="22,6 25,15 34,15 27,21 30,30 22,24 14,30 17,21 10,15 19,15"/><polygon points="7,16 8.5,20 13,20 9.5,23 11,27 7,24.5 3,27 4.5,23 1,20 5.5,20" transform="translate(0,2)"/><polygon points="37,16 38.5,20 43,20 39.5,23 41,27 37,24.5 33,27 34.5,23 31,20 35.5,20" transform="translate(0,2)"/></svg>
    <h3>5-Star Travel Planning for Every Budget</h3>
    <p>White-glove service and exceptional travel planning is our motto.</p>
  </div>
  <div class="feature f2">
    <svg viewBox="0 0 44 44" fill="none" stroke="#fff" stroke-width="2"><circle cx="22" cy="22" r="16"/><path d="M28 16l-4 8-8 4 4-8z"/></svg>
    <h3>A Travel Itinerary Engineered Just For You</h3>
    <p>Trelmavista caters to all needs. Using points? Lounge access? No problem. We mastered the art of optimizing miles.</p>
  </div>
  <div class="feature f3">
    <svg viewBox="0 0 44 44" fill="none" stroke="#fff" stroke-width="2.5"><circle cx="22" cy="22" r="15"/><path d="M11 11l22 22"/></svg>
    <h3>Avoid Common Traveler Mistakes</h3>
    <p>While planning or vacationing, it is easy to make costly mistakes. Let us remove that worry!</p>
  </div>
  <div class="feature f4">
    <svg viewBox="0 0 44 44" fill="none" stroke="#fff" stroke-width="2"><circle cx="22" cy="22" r="15"/><path d="M26 16c-2-2-9-2-9 2s9 2 9 6-7 4-9 2M21.5 12v20"/></svg>
    <h3>Save Time &amp; Money</h3>
    <p>A sound travel itinerary takes dedication &amp; commitment, qualities that we provide for each handcrafted journey.</p>
  </div>
</div>

<!-- services -->
<h2 class="abs section-title" style="top:1070px">What Can our travel engineers<br>help you plan?</h2>

<div class="abs service-card" style="left:121px">
  <div class="service-photo" style="background:radial-gradient(circle at 50% 40%,#e7b38a,#9b6a48)" role="img" aria-label="Photo of a smiling traveller in a hat by a vintage car"></div>
  <h3>Personal Trip</h3>
  <p>Get your personalized itinerary from an expert travel engineer and access it anywhere.</p>
  <a class="more">Learn More</a>
</div>
<div class="abs service-card raised" style="left:446px">
  <div class="service-photo" style="background:linear-gradient(180deg,#d8d1c6,#7b766f)" role="img" aria-label="Photo of a business traveller pulling a rolling suitcase"></div>
  <h3>Business Trip</h3>
  <p>Get a tailored sightseeing itinerary while on-the-go for business.</p>
  <a class="more">Learn More</a>
</div>
<div class="abs service-card" style="left:770px">
  <div class="service-photo" style="background:radial-gradient(circle at 50% 45%,#f2f2ee,#b9bdb0)" role="img" aria-label="Photo of an elegant event table set with glasses and flowers"></div>
  <h3>Overseas Event</h3>
  <p>Get recommendations and logistics guidance for your overseas events.</p>
  <a class="more">Learn More</a>
</div>

<!-- how it works -->
<div class="abs how"></div>
<svg class="abs" style="left:0;top:1740px" width="1200" height="60" viewBox="0 0 1200 60"><path fill="#ede5da" d="M0 60V30l16-8 14 12 18-14 16 10 20-6 22 12 30-10 26 8 40-6 40 10 60-8 80 6 100-4 120 6 100-6 100 4 80-8 60 8 50-10 40 6 30-8 28 10 24-12 20 8 16-10 20 12 14-8 16 6V60z"/></svg>

<svg class="abs" style="left:426px;top:2187px" width="346" height="172" viewBox="0 0 346 172"><path d="M0 172A173 172 0 0 1 346 172z" fill="#a88a63"/></svg>
<div class="abs center" style="left:426px;top:2300px;width:346px;color:#fff;font-weight:700;font-size:16px;letter-spacing:1px">TRELMAVISTA</div>
<svg class="abs" style="left:580px;top:2150px" width="40" height="52" viewBox="0 0 40 52"><path d="M20 50C8 32 2 24 2 17a18 18 0 0 1 36 0c0 7-6 15-18 33z" fill="#4d3613"/><circle cx="20" cy="17" r="6" fill="#fff"/></svg>
<svg class="abs" style="left:0;top:1990px" width="1200" height="369" viewBox="0 0 1200 369" fill="none" stroke="#c9bcaa" stroke-dasharray="3 5"><path d="M380 230L540 300M480 140L560 260M599 105V220M720 140L640 260M820 230L660 300"/></svg>

<div class="abs step-label" style="left:144px;top:2140px">Select The Service</div>
<div class="abs step" style="left:189px;top:2158px;background:var(--espresso)"><div class="step-inner"><svg width="40" height="40" viewBox="0 0 40 40" fill="none" stroke="#cda050" stroke-width="4"><path d="M8 21l8 8 16-18"/></svg></div></div>
<div class="abs num" style="left:366px;top:2260px;color:var(--espresso)">01</div>

<div class="abs step-label" style="left:262px;top:1962px">Complete the Survey</div>
<div class="abs step" style="left:312px;top:1984px;background:var(--bronze)"><div class="step-inner"><svg width="34" height="38" viewBox="0 0 34 38" fill="none" stroke="#7d6236" stroke-width="2.5"><rect x="5" y="3" width="24" height="32" rx="2"/><path d="M10 12h14M10 18h14M10 24h9"/></svg></div></div>
<div class="abs num" style="left:446px;top:2144px;color:var(--bronze)">02</div>

<div class="abs step-label" style="left:475px;top:1893px">Connect with a Travel Engineer</div>
<div class="abs step" style="left:520px;top:1915px;background:var(--taupe)"><div class="step-inner"><svg width="42" height="34" viewBox="0 0 42 34" fill="none" stroke="#b59569" stroke-width="2.5"><circle cx="15" cy="11" r="6"/><circle cx="28" cy="11" r="6"/><path d="M4 31c0-7 5-11 11-11s11 4 11 11zM24 20c7 0 14 3 14 11H26"/></svg></div></div>
<div class="abs num" style="left:584px;top:2102px;color:var(--taupe)">03</div>

<div class="abs step-label" style="left:688px;top:1962px">Access Custom Itinerary</div>
<div class="abs step" style="left:730px;top:1984px;background:var(--gold)"><div class="step-inner"><svg width="30" height="38" viewBox="0 0 30 38" fill="none" stroke="#cda050" stroke-width="2.5"><rect x="4" y="16" width="22" height="18" rx="3"/><path d="M9 16v-5a6 6 0 0 1 12 0v5M15 23v4"/></svg></div></div>
<div class="abs num" style="left:719px;top:2144px;color:var(--gold)">04</div>

<div class="abs step-label" style="left:810px;top:2143px">Travel Worry-Free</div>
<div class="abs step" style="left:855px;top:2162px;background:var(--butter)"><div class="step-inner"><svg width="28" height="38" viewBox="0 0 28 38" fill="none" stroke="#4d3613" stroke-width="2.5"><rect x="5" y="6" width="18" height="28" rx="4"/><path d="M10 6V2h8v4M10 14h8M10 20h8M10 26h8"/></svg></div></div>
<div class="abs num" style="left:800px;top:2260px;color:var(--butter)">05</div>

<div class="abs ready"></div>
<h2 class="abs section-title" style="top:2424px;color:var(--white)">Ready to Get Planning?</h2>
<a class="abs btn" style="left:518px;top:2490px;width:162px;height:41px;line-height:41px">Get Started</a>

<!-- ambassadors -->
<h2 class="abs section-title" style="top:2686px">Experiences Curated with Inspiration<br>From Our Brand Ambassadors</h2>
<div class="abs arrow" style="left:57px;top:2913px"><svg width="36" height="36" viewBox="0 0 36 36" fill="none" stroke="#c9beb1" stroke-width="2"><path d="M24 18H12M17 12l-6 6 6 6"/></svg></div>
<div class="abs arrow" style="left:1101px;top:2913px"><svg width="36" height="36" viewBox="0 0 36 36" fill="none" stroke="#c9beb1" stroke-width="2"><path d="M12 18h12M19 12l6 6-6 6"/></svg></div>

<div class="abs amb" style="left:114px;top:2824px"><div class="amb-photo" style="background:linear-gradient(180deg,#8aa8c6,#c9a48c)" role="img" aria-label="Portrait of ambassador Martin Hale"></div><h4>MARTIN HALE</h4><span style="font-size:13px">Author &amp; TV Personality</span></div>
<div class="abs amb" style="left:359px;top:2824px"><div class="amb-photo" style="background:linear-gradient(180deg,#ece3d6,#b58668)" role="img" aria-label="Portrait of ambassador Colette Ravel"></div><h4>COLETTE RAVEL</h4><span>French Lifestyle Influencer</span></div>
<div class="abs amb" style="left:604px;top:2824px"><div class="amb-photo" style="background:linear-gradient(180deg,#c8ad8a,#4e4138)" role="img" aria-label="Portrait of ambassador Luca Ferrant"></div><h4>LUCA FERRANT</h4><span>Founder &amp; CEO</span></div>
<div class="abs amb" style="left:850px;top:2824px"><div class="amb-photo" style="background:linear-gradient(180deg,#8a5a44,#3a2a24)" role="img" aria-label="Portrait of ambassador Marina Solde"></div><h4>MARINA SOLDE</h4><span>Italian Singer</span></div>

<!-- resources -->
<div class="abs res-bg"></div>
<svg class="abs" style="left:0;top:3186px" width="1200" height="40" viewBox="0 0 1200 40"><path fill="#ede5da" d="M0 40V22l20-6 18 8 24-10 30 8 40-6 60 6 100-4 140 6 200-6 160 4 120-6 80 8 60-8 40 6 30-10 26 8 24-8 28 10V40z"/></svg>
<h2 class="abs section-title" style="top:3304px">Start With Our Free Travel Resources</h2>

<div class="abs post" style="left:118px">
  <div class="post-photo" style="background:linear-gradient(180deg,#7fa9d8,#6f6a5e 70%,#5a5448)" role="img" aria-label="Photo of a red pagoda with a mountain behind"><div class="date">Jan 19</div></div>
  <h4>2020 Japan Travel Guide <em>4 ♡</em></h4>
  <p>Japan, the land of the rising sun &amp; robotics! What a truly exceptional destination. I must be honest, Japan was not in my top 10 countries to visit, but af....</p>
  <a class="more">Read More</a>
</div>
<div class="abs post" style="left:442px">
  <div class="post-photo" style="background:linear-gradient(180deg,#9fb2c6,#9b7a5c 45%,#a0603e)" role="img" aria-label="Photo of a hillside city with terracotta roofs"><div class="date">Jan 04</div></div>
  <h4>2020 Peru Travel Guide: Hiking Machu Picchu (Inca Trail) <em>8 ♡</em></h4>
  <p style="margin-top:14px">Quintessentially bucolic, Peru attracts foodies, hikers, history-buffs and nature-lovers alike. If you are going to Peru for the first time and are getting overwhelmed b....</p>
  <a class="more">Read More</a>
</div>
<div class="abs post" style="left:767px">
  <div class="post-photo" style="background:linear-gradient(180deg,#9cc0e2,#b89c78 40%,#6e5a44)" role="img" aria-label="Photo of a historic mosque street in Cairo"><div class="date">Jan 03</div></div>
  <h4>2020 Egypt Travel Guide <em>10 ♡</em></h4>
  <p>Home to the last of the seven wonders of the ancient world, Egypt is as mysterious as it is breathtaking. With a history that stretches as far back as we hav...</p>
  <a class="more">Read More</a>
</div>

<!-- newsletter -->
<h2 class="abs section-title" style="top:4136px">Subscribe our Newsletter</h2>
<div class="abs news"><span>Email Address</span><a class="btn">Subscribe Now</a></div>

<!-- footer -->
<div class="abs footer"></div>
<svg class="abs" style="left:0;top:4318px" width="1200" height="40" viewBox="0 0 1200 40"><path fill="#a88a63" d="M0 40V18l18 8 20-10 24 8 30-6 40 8 80-6 120 4 160-6 200 6 160-4 120 6 80-8 50 8 40-10 30 8 28-6V40z"/></svg>
<div class="abs" style="left:122px;top:4590px;color:#4d3613;font-weight:700;font-size:18px">TRELMAVISTA</div>
<svg class="abs" style="left:120px;top:4626px" width="26" height="26" viewBox="0 0 26 26" fill="none" stroke="#fff" stroke-width="1.6"><rect x="3" y="7" width="20" height="14" rx="2"/><path d="M3 8l10 7 10-7"/></svg>
<div class="abs" style="left:162px;top:4634px;font-size:12px;color:#fff">Questions? Contact Us.</div>

<div class="abs foot-col" style="left:402px;top:4526px"><h5>Services</h5><a>Personal Trip Planning</a><a>Business Trip Planning</a><a>Overseas Event Planning</a></div>
<div class="abs foot-col" style="left:601px;top:4526px"><h5>Short Links</h5><a>Free Travel Resources</a><a>Terms and Conditions</a><a>Privacy Policy</a></div>
<div class="abs foot-col" style="left:803px;top:4526px;width:290px"><h5>About us</h5><a style="line-height:31px;margin-top:-8px">Trelmavista's mission is to engineer personalized, handcrafted travel itineraries and event plans for travelers worldwide.</a></div>

<div class="abs" style="left:120px;top:4727px;width:958px;height:2px;background:#fff"></div>
<div class="abs" style="left:120px;top:4766px;font-size:12px;color:#fff">Copyright ©Trelmavista. 2020. All Rights Reserved.</div>
<svg class="abs" style="left:1032px;top:4750px" width="44" height="44" viewBox="0 0 44 44"><circle cx="22" cy="22" r="20" fill="none" stroke="#fff" stroke-width="2"/></svg>

</body>
</html>
```